Young and modern Electrical company working in the commercial arena.

Wanting a business card design thats modern and will last. Maybe Minimalist? Happy to look at changing my logo

Target Market(s)

Builders, Project Managers

Industry/Entity Type

Electrical

Contact Information for Business Card

Name
Address
Phone number
Job title

Logo Text

our name or just the logo i'm open to ideas

Font styles to use
Sans Serif

Requirements
Nice to have
• would like to keep the purple in our current logo. it's kinda unique to our market
Should not have
• Don't want it to be to busy. simple is best i think

```html
<!DOCTYPE html>
<html lang="en">
<head>
<meta charset="utf-8">
<title>Halden Electrical – Business Card</title>
<link href="https://fonts.googleapis.com/css2?family=Lato:wght@700&display=swap" rel="stylesheet">
<style>
  :root {
    --brand-purple: #6a3d98;
    --card-white: #ffffff;
    --name-lilac: #c5bdcc;
    --contact-grey: #978ca3;
  }
  html, body {
    margin: 0;
    padding: 0;
    overflow: hidden;
    background: var(--card-white);
  }
  .card {
    position: relative;
    width: 1200px;
    height: 689px;
    background: var(--card-white);
    overflow: hidden;
    font-family: "Lato", sans-serif;
    font-weight: 700;
  }
  .band {
    position: absolute;
    left: 0;
    width: 100%;
    background: var(--brand-purple);
  }
  .band--top { top: 0; height: 43px; }
  .band--bottom { bottom: 0; height: 48px; }
  .holder-name {
    position: absolute;
    top: 143px;
    left: 0;
    width: 100%;
    margin: 0;
    text-align: center;
    font-size: 115px;
    font-weight: 700;
    line-height: 1;
    letter-spacing: 1px;
    color: var(--name-lilac);
  }
  .company-name {
    position: absolute;
    top: 309px;
    left: 0;
    width: 100%;
    margin: 0;
    text-align: center;
    font-size: 40px;
    line-height: 1;
    color: var(--name-lilac);
  }
  .contact-list {
    position: absolute;
    top: 385px;
    left: 0;
    width: 100%;
    margin: 0;
    padding: 0;
    list-style: none;
    text-align: center;
    font-size: 43px;
    line-height: 51px;
    color: var(--contact-grey);
  }
</style>
</head>
<body>
  <main class="card">
    <div class="band band--top"></div>
    <h1 class="holder-name">JOHN DOE</h1>
    <p class="company-name">Halden Electrical</p>
    <ul class="contact-list">
      <li class="contact-email">email@sparkmail.com</li>
      <li class="contact-web">www.haldenworks.com</li>
      <li class="contact-phone">P: 0800 4 VOLTS</li>
      <li class="contact-mobile">C: 0215550147</li>
    </ul>
    <div class="band band--bottom"></div>
  </main>
</body>
</html>
```